Need Amazing Website for Consulting Company

We need an amazing website design for a Human Resources Consulting Company. This will be geared towards a more professional crowd, but we don't want it to be overly corporate and stuffy: Just, clean and professional and amazing. Please use the video link below for further instruction.

http://clipvesta.net/v/kqPzRmN4

Thank You.

PS Logo file has been attached.

Target Market(s)

The target marketing is small business owners who have employees. These owners cant afford an in-house HR person so they would hire this client to consult and do the work for them.

Industry/Entity Type

It Company

Font styles to use
Sans Serif

Requirements
Must have
• Please watch video:

Must have spot for video on homepage.
Nice to have
• Clean, professional, but not overly corporate, we want a personal and fun feel to this site a bit to separate them from all the other executive type sites. This site should have some LIFE to it and reflect a local brand that is doing great things.
Should not have
• Should not be just a corporate site, should not be overly stuffy, should not be overly boring.

```html
<!DOCTYPE html>
<html lang="en">
<head>
<meta charset="utf-8">
<title>Mesa Ridge HR Consulting</title>
<link href="https://fonts.googleapis.com/css2?family=Open+Sans:ital,wght@0,300;0,400;0,600;0,700;1,400&family=Roboto+Condensed:wght@300;400;700&display=swap" rel="stylesheet">
<style>
:root{
  --red:#b71c2e;
  --red-dark:#96121f;
  --red-light:#cf2b3d;
  --blue:#1560c0;
  --blue-deep:#0a2f72;
  --nav-active:#16396d;
  --ink:#1c1c1c;
  --grey-text:#666;
  --grey-light:#9a9a9a;
  --page:#ebebeb;
  --card:#f4f4f6;
  --white:#fff;
}
*{margin:0;padding:0;box-sizing:border-box}
html,body{width:1200px;height:1124px;overflow:hidden}
body{position:relative;background:var(--page);font-family:"Open Sans",sans-serif;color:var(--ink)}

.site-header{position:absolute;left:0;top:0;width:1200px;height:140px;background:linear-gradient(#fff,#f1f1f1)}
.brand{position:absolute;left:150px;top:30px;display:flex;align-items:center;gap:12px}
.brand-name{font-family:"Open Sans",sans-serif;font-weight:700;font-size:27px;line-height:31px;color:var(--ink);width:170px}
.brand-mark{width:40px;height:40px;border-radius:50%;background:var(--red)}
.call{position:absolute;left:838px;top:49px;display:flex;align-items:center;gap:12px}
.call-icon{width:46px;height:46px;border:2px solid #222;border-radius:50%;display:flex;align-items:center;justify-content:center}
.call-label{font-size:17px;color:#666;line-height:20px}
.call-number{font-family:"Roboto Condensed",sans-serif;font-weight:700;font-size:25px;color:#111;line-height:28px;letter-spacing:.5px}

.main-nav{position:absolute;left:0;top:140px;width:1200px;height:48px;background:linear-gradient(var(--red-light),var(--red) 55%,var(--red-dark))}
.main-nav ul{list-style:none;position:absolute;left:150px;top:0;display:flex;height:48px}
.main-nav li{font-family:"Roboto Condensed",sans-serif;font-size:19px;color:#fff;height:48px;line-height:48px;text-align:center;border-right:1px solid rgba(0,0,0,.25);box-shadow:1px 0 0 rgba(255,255,255,.12)}
.main-nav li:last-child{border:none;box-shadow:none}
.main-nav li.is-active{background:linear-gradient(#1e4a85,var(--nav-active))}

.hero{position:absolute;left:0;top:188px;width:1200px;height:309px;background:radial-gradient(ellipse 60% 90% at 35% 45%,#2a7ddc,var(--blue) 45%,var(--blue-deep))}
.hero-title{position:absolute;left:150px;top:72px;font-family:"Roboto Condensed",sans-serif;font-weight:300;font-size:34px;color:#fff;letter-spacing:.3px}
.hero-text{position:absolute;left:150px;top:118px;width:420px;font-size:14.5px;line-height:23px;color:#fff}
.btn-more{position:absolute;left:150px;top:208px;width:175px;height:39px;background:linear-gradient(var(--red-light),var(--red-dark));border-radius:2px;color:#fff;font-weight:700;font-size:15px;line-height:39px;text-align:center;box-shadow:0 1px 3px rgba(0,0,0,.4)}
.slider-dots{position:absolute;left:150px;top:525px;display:flex;gap:5px}
.slider-dots span{width:14px;height:14px;border-radius:50%;background:#ddd;border:1px solid #aaa}
.slider-dots span.is-current{background:var(--red);border-color:var(--red-dark)}

.video-frame{position:absolute;left:574px;top:242px;width:459px;height:316px;background:#fff;padding:10px;box-shadow:0 6px 12px rgba(0,0,0,.3)}
.video-still{width:100%;height:100%;background:radial-gradient(ellipse at 50% 40%,#fafafa,#d6d6d6 70%,#aaa);display:flex;align-items:center;justify-content:center;box-shadow:inset 0 0 20px rgba(0,0,0,.35)}
.play-btn{width:54px;height:54px;border-radius:50%;background:rgba(255,255,255,.55);border:3px solid rgba(255,255,255,.9);display:flex;align-items:center;justify-content:center;margin-top:-30px}

.services-head{position:absolute;left:0;top:624px;width:1200px;text-align:center}
.services-title{display:inline-flex;align-items:center;gap:14px;font-size:21px;font-weight:600;color:#333;letter-spacing:.3px}
.services-title::before,.services-title::after{content:"";width:140px;height:1px;background:#ccc}
.services-sub{font-size:16px;font-weight:300;color:var(--grey-light);margin-top:10px}

.service-card{position:absolute;top:724px;width:280px;height:304px;background:var(--card);border:1px solid #d4d4d4}
.service-card h3{height:48px;background:linear-gradient(#3a3a3a,#000);color:#fff;font-size:16px;font-weight:700;line-height:48px;padding-left:20px}
.service-card ul{list-style:none;padding:24px 0 0 26px}
.service-card li{font-size:12.5px;color:var(--grey-text);height:27.3px;display:flex;align-items:center;gap:14px}
.service-card li::before{content:"";width:5px;height:5px;border:1px dotted #888;transform:rotate(45deg)}
.view-more{position:absolute;left:20px;bottom:16px;font-size:13px;font-style:italic;color:var(--red)}

.site-footer{position:absolute;left:0;top:1076px;width:1200px;height:48px;background:linear-gradient(var(--red-light),var(--red))}
.copyright{position:absolute;left:150px;top:16px;font-size:12px;color:#fff}
.social{position:absolute;left:905px;top:15px;display:flex;gap:15px}
.social span{width:18px;height:18px;border-radius:50%;background:rgba(0,0,0,.35)}
</style>
</head>
<body>
<header class="site-header">
  <div class="brand"><span class="brand-name">Mesa Ridge HR Consulting</span><span class="brand-mark"></span></div>
  <div class="call">
    <div class="call-icon"><svg width="22" height="22" viewBox="0 0 24 24"><path d="M6.6 10.8a15 15 0 0 0 6.6 6.6l2.2-2.2a1 1 0 0 1 1-.25 11 11 0 0 0 3.6.6 1 1 0 0 1 1 1V20a1 1 0 0 1-1 1A17 17 0 0 1 3 4a1 1 0 0 1 1-1h3.5a1 1 0 0 1 1 1c0 1.25.2 2.45.57 3.57a1 1 0 0 1-.25 1z" fill="#222"/></svg></div>
    <div><div class="call-label">Questions? Call us at</div><div class="call-number">(123) - &nbsp;456 - 7890</div></div>
  </div>
</header>

<nav class="main-nav">
  <ul>
    <li class="is-active" style="width:94px">HOME</li>
    <li style="width:122px">ABOUT US</li>
    <li style="width:121px">SERVICES</li>
    <li style="width:120px">STAFFING</li>
    <li style="width:124px">PARTNERS</li>
    <li style="width:131px">OUR TEAM</li>
    <li style="width:134px">CONTACT US</li>
  </ul>
</nav>

<section class="hero">
  <h1 class="hero-title">Consectetur &nbsp;Vestibulum</h1>
  <p class="hero-text">Lorem Ipsum is simply dummy text of the printing and typesetting industry Lorem Ipsum has been the industry's standard dummy text ever since when an unknown printer.</p>
  <div class="btn-more">MORE INFORMATION</div>
</section>
<div class="slider-dots"><span></span><span class="is-current"></span><span></span><span></span></div>

<div class="video-frame">
  <div class="video-still" role="img" aria-label="Company introduction video still">
    <div class="play-btn"><svg width="20" height="22" viewBox="0 0 20 22"><path d="M3 1l16 10L3 21z" fill="#fff"/></svg></div>
  </div>
</div>

<section class="services-head">
  <h2 class="services-title">MESA RIDGE SERVICES</h2>
  <p class="services-sub">Dolor sit amet, consectetur adipiscing Vestibulum ultrices tellus mi</p>
</section>

<article class="service-card" style="left:148px">
  <h3>LOREM IPSUM DOLOR</h3>
  <ul><li>Lorem Ipsum is simply dummy text</li><li>Lorem Ipsum has been the</li><li>Tndustry's standard dummy text</li><li>Ever since the 1500s, when an</li><li>Unknown printer took a galley of</li><li>Specimen book. It has</li><li>Only five centuries, but also</li></ul>
  <span class="view-more">View more →</span>
</article>
<article class="service-card" style="left:460px">
  <h3>LOREM IPSUM DOLOR</h3>
  <ul><li>Lorem Ipsum is simply dummy text</li><li>Lorem Ipsum has been the</li><li>Tndustry's standard dummy text</li><li>Ever since the 1500s, when an</li><li>Unknown printer took a galley of</li><li>Specimen book. It has</li><li>Only five centuries, but also</li></ul>
  <span class="view-more">View more →</span>
</article>
<article class="service-card" style="left:770px">
  <h3>LOREM IPSUM DOLOR</h3>
  <ul><li>Lorem Ipsum is simply dummy text</li><li>Lorem Ipsum has been the</li><li>Tndustry's standard dummy text</li><li>Ever since the 1500s, when an</li><li>Unknown printer took a galley of</li><li>Specimen book. It has</li><li>Only five centuries, but also</li></ul>
  <span class="view-more">View more →</span>
</article>

<footer class="site-footer">
  <p class="copyright">Copyright © 2014 Mesa Ridge Consulting. All Rights Reserved.</p>
  <div class="social"><span></span><span></span><span></span><span></span><span></span></div>
</footer>
</body>
</html>
```